Freelancers in the field of IT security and IT service need a business card design

I need a business card design for my company. I am a freelancer and active in the area of IT security, IT support% 26 # 252; tung, consulting. I am not yet color-coded, but it should be a modern color that can also be used for a later website. The design should be innovation. Exude dynamism and reliability

Target Market(s)

IT security, IT solutions

Contact Information for Business Card

Firma: brandel-advisory, Inhaber: Jonas Wirtel
Adresse: Lindenhang 4, D-73218 Feldrachingen
Telefon: +49 (0) 7354 608193
E-Mail Jonas.Wirtel@brandel-advisory.example

```html
<!DOCTYPE html>
<html lang="de">
<head>
<meta charset="utf-8">
<title>brandel-advisory – Visitenkarte</title>
<link rel="stylesheet" href="https://fonts.googleapis.com/css2?family=Roboto:wght@400;500;700&display=swap">
<style>
  :root {
    --brand-blue: #0b4279;
    --paper: #f1f2f3;
    --stage: #e4e4e2;
    --rule-grey: #5a5a5a;
    --band-grey: #8a8d93;
    --text-grey: #4a4a4a;
    --logo-light: #e9edf2;
  }
  * { box-sizing: border-box; margin: 0; padding: 0; }
  html, body {
    width: 1200px; height: 960px; overflow: hidden;
    background: var(--stage);
    font-family: "Roboto", Arial, sans-serif;
  }
  .canvas { position: relative; width: 1200px; height: 960px; }

  .card {
    position: absolute;
    width: 560px; height: 320px;
    box-shadow: 0 2px 6px rgba(0,0,0,0.12);
    overflow: hidden;
  }

  /* Front face */
  .card--front {
    left: 120px; top: 130px;
    background: var(--brand-blue);
  }
  .card--front .brand-name {
    position: absolute; left: 0; right: 0; top: 142px;
    text-align: center;
    color: var(--logo-light);
    font-weight: 500; font-size: 30px; letter-spacing: 1px;
  }

  /* Back face */
  .card--back {
    left: 520px; top: 500px;
    background: var(--paper);
  }
  .card--back .brand-name {
    position: absolute; right: 44px; top: 48px;
    color: var(--brand-blue);
    font-weight: 500; font-size: 24px; letter-spacing: 1px;
  }
  .side-tab {
    position: absolute; left: 0; top: 168px;
    width: 20px; height: 44px;
    background: var(--brand-blue);
  }
  .person { position: absolute; left: 52px; top: 140px; }
  .person__name {
    color: var(--brand-blue);
    font-weight: 700; font-size: 30px; line-height: 1;
  }
  .person__role {
    color: var(--text-grey);
    font-weight: 700; font-size: 15px; margin-top: 3px;
  }
  .name-rule {
    position: absolute; left: 250px; right: 40px; top: 166px;
    height: 1.5px; background: var(--rule-grey);
  }
  .contact {
    position: absolute; left: 52px; top: 208px;
    list-style: none;
    color: var(--text-grey); font-size: 15px;
  }
  .contact li { display: flex; align-items: center; gap: 8px; height: 22px; white-space: nowrap; }
  .contact svg { width: 14px; height: 14px; fill: var(--brand-blue); flex: none; }
  .bottom-band {
    position: absolute; left: 0; right: 0; bottom: 0; height: 10px;
    display: flex;
  }
  .bottom-band__blue { width: 66%; background: var(--brand-blue); }
  .bottom-band__grey { flex: 1; background: var(--band-grey); }
</style>
</head>
<body>
<main class="canvas">
  <section class="card card--front" aria-label="Vorderseite">
    <div class="brand-name">BRANDEL-ADVISORY</div>
  </section>

  <section class="card card--back" aria-label="Rückseite">
    <div class="brand-name">BRANDEL-ADVISORY</div>
    <div class="side-tab"></div>
    <div class="person">
      <div class="person__name">Jonas Wirtel</div>
      <div class="person__role">Director</div>
    </div>
    <div class="name-rule"></div>
    <ul class="contact">
      <li>
        <svg viewBox="0 0 16 16" aria-hidden="true"><path d="M3 2h3l1.5 3.5-2 1.2a8 8 0 0 0 3.8 3.8l1.2-2L14 10v3a1 1 0 0 1-1 1A11 11 0 0 1 2 3a1 1 0 0 1 1-1z"/></svg>
        +49 (0) 7354 608193
      </li>
      <li>
        <svg viewBox="0 0 16 16" aria-hidden="true"><path d="M1 3h14v10H1zM2.5 4.5 8 9l5.5-4.5V12h-11z" fill-rule="evenodd"/></svg>
        Jonas.Wirtel@brandel-advisory.example
      </li>
      <li>
        <svg viewBox="0 0 16 16" aria-hidden="true"><path d="M8 1a5 5 0 0 1 5 5c0 3.5-5 9-5 9S3 9.5 3 6a5 5 0 0 1 5-5zm0 3a2 2 0 1 0 0 4 2 2 0 0 0 0-4z" fill-rule="evenodd"/></svg>
        Lindenhang 4, D-73218 Feldrachingen
      </li>
    </ul>
    <div class="bottom-band">
      <div class="bottom-band__blue"></div>
      <div class="bottom-band__grey"></div>
    </div>
  </section>
</main>
</body>
</html>
```